Skincare Cleanser Bottle Label

New product launch of a mint facial cleanser.
Brand is called Dorvelle.
Product will be called Lunara.
Looking for a label design that can be printed using silk screening.
High gloss white plastic bottle. 8oz. White push pump top.
Clinical skincare brand, professional image, sold in medical spas.

Target Market(s)

Women Age 20-65

Industry/Entity Type

Health And Wellness

Font styles to use
Serif
Sans Serif

Requirements
Must have
• Dorvelle brand name in the orignal font.
Should not have
• Multiple colours.

```html
<!DOCTYPE html>
<html lang="en">
<head>
<meta charset="utf-8">
<title>Dorvelle Lunara Label Options</title>
<link href="https://fonts.googleapis.com/css2?family=Montserrat:wght@400;600;700&family=Open+Sans:wght@400&display=swap" rel="stylesheet">
<style>
  :root {
    --ink: #111111;
    --paper: #ffffff;
    --backdrop: #d9d9d9;
    --rule: #cfcfcf;
    --mint-light: #f2f2f2;
    --mint-dark: #9a9a9a;
  }
  html, body {
    margin: 0;
    padding: 0;
    width: 1200px;
    height: 1200px;
    overflow: hidden;
    background: var(--backdrop);
    font-family: "Montserrat", sans-serif;
    color: var(--ink);
  }
  .canvas {
    position: relative;
    width: 1200px;
    height: 1200px;
  }
  .label {
    position: absolute;
    top: 296px;
    width: 308px;
    height: 790px;
    background: var(--paper);
    border: 1px solid var(--rule);
    box-sizing: border-box;
    overflow: hidden;
  }
  .label--regular { left: 165px; }
  .label--bold { left: 667px; }
  .brand-name {
    position: absolute;
    left: 2px;
    bottom: 40px;
    writing-mode: vertical-rl;
    transform: rotate(180deg);
    font-family: "Montserrat", sans-serif;
    font-weight: 400;
    font-size: 118px;
    line-height: 1;
    letter-spacing: -3px;
    color: var(--ink);
    margin: 0;
  }
  .product-tag {
    position: absolute;
    left: 109px;
    top: 336px;
    width: 193px;
    height: 64px;
    background: var(--ink);
    color: var(--paper);
    display: flex;
    align-items: center;
    justify-content: center;
    font-size: 30px;
    letter-spacing: 0.5px;
    margin: 0;
  }
  .label--regular .product-tag { font-weight: 600; }
  .label--bold .product-tag { font-weight: 700; }
  .product-type {
    position: absolute;
    left: 109px;
    top: 410px;
    width: 193px;
    text-align: center;
    font-family: "Open Sans", sans-serif;
    font-size: 15px;
    margin: 0;
  }
  .mint-art {
    position: absolute;
    left: 172px;
    top: 514px;
    width: 136px;
    height: 186px;
    background: radial-gradient(circle at 60% 50%, var(--mint-dark), var(--mint-light) 75%);
    border-radius: 40% 0 0 50%;
  }
  .volume {
    position: absolute;
    left: 0;
    width: 100%;
    top: 756px;
    text-align: center;
    font-size: 9px;
    margin: 0;
  }
  .annotation {
    position: absolute;
    top: 0;
    left: 0;
  }
  .annotation-text {
    position: absolute;
    font-weight: 700;
    font-size: 18px;
    letter-spacing: 1px;
    margin: 0;
  }
  .annotation-text--regular { left: 499px; top: 608px; }
  .annotation-text--bold { left: 1070px; top: 557px; }
  .option-number {
    position: absolute;
    top: 1138px;
    font-family: "Open Sans", sans-serif;
    font-size: 26px;
    margin: 0;
  }
  .option-number--a { left: 288px; }
  .option-number--b { left: 790px; }
</style>
</head>
<body>
<main class="canvas">
  <section class="label label--regular">
    <h1 class="brand-name">dorvelle</h1>
    <p class="product-tag">LUNARA</p>
    <p class="product-type">MINT FACIAL CLEANSER</p>
    <div class="mint-art" role="img" aria-label="Black line illustration of mint leaves"></div>
    <p class="volume">8.5 OZ / 250 ML</p>
  </section>

  <section class="label label--bold">
    <h1 class="brand-name">dorvelle</h1>
    <p class="product-tag">LUNARA</p>
    <p class="product-type">MINT FACIAL CLEANSER</p>
    <div class="mint-art" role="img" aria-label="Black line illustration of mint leaves"></div>
    <p class="volume">8.5 OZ / 250 ML</p>
  </section>

  <svg class="annotation" width="1200" height="1200" viewBox="0 0 1200 1200" aria-hidden="true">
    <path d="M474 652 C476 600 478 560 496 556 C516 552 524 592 540 592 C552 592 556 578 556 570"
          fill="none" stroke="#111" stroke-width="1.5"/>
    <path d="M975 652 C977 600 979 560 997 556 C1015 552 1023 594 1039 594 C1052 594 1056 582 1057 574"
          fill="none" stroke="#111" stroke-width="1.5"/>
  </svg>
  <p class="annotation-text annotation-text--regular">REGULAR</p>
  <p class="annotation-text annotation-text--bold">BOLD</p>

  <p class="option-number option-number--a">10 a</p>
  <p class="option-number option-number--b">10 b</p>
</main>
</body>
</html>
```